Campaign Flyer for a local election

Black and white election flyer

See information below to be included:

Re-elect Morton
Experienced Glenmoor Board Member
Experienced NYC Principal
Experienced leader

One Year Board Accomplishments:
-Installed New Park Lights (Bollards)
-Red Brick Road Repair Project
-Established Closer Ties with Our local precinct to frequently monitor the community with directed security patrols. Requested an increased police presence.
-Met with the 82nd Precinct Officials & Assemblywoman, Linda Marwick to discuss our security issues
- Focused on maintenance of streetlights to make brighter streets
-Negotiated Contract & Hired Our New Landscaper, Hollowfield Landscapers
-Major Homeowner Shrub Replacement Project
- Addressing Standing Water in our Park (Installed French Drain)
- Replaced and upgraded all 5 outdoor circuit breaker panels
-Write monthly community newsletters
-Sewer cleaning project (had all community catch basins cleaned)
-Carefully overseeing our new school project. Coordinating with the sponsor and the school directors
-Delivered a very healthy budget to the community
-Works closely with our committees
-Events: Zoo event, Petting Zoo, Outdoor Movie Night, Egg Hunt

It is my intent to seek re-election.
(Photo) Morton Velasquez
-Dedicated to improving our community
-Hard-working…He gets thing done!
-Trustworthy

. .

Please note, I am submitting new information under accomplishments. The list of accomplishments should be in the same sequence, starting with: Met with the 82nd Precinct....
Please carefully review.
----------------------------------------------------------------------------------------------------------------------------------------------------------------

Re-elect Morton
Experienced NYC Principal
Experienced leader

Last Year’s Board Accomplishments:

-Met with the 82nd Precinct Officials & Assemblywoman, Linda Marwick, to discuss our security issues. Requested increased police presence.
-Established a strong partnership with the 82nd precinct to frequently monitor the community with directed security patrols.
-Replaced all new park lights (Bollards) to make the park brighter
- Focused on maintenance of streetlights to make streets brighter
-‘Fixing Our Streets Project’ (Repaired all cracked/missing red bricks)
-Homeowner Shrub Replacement Project (Replaced hundreds of bushes)
- I write the monthly community newsletter
-Carefully overseeing our new school project. Coordinating with the sponsor and the school director
-Monitoring C of O’s and homeowners Insurance

(Photo) Morton Velasquez
-Hard-working! I get things done!
-Trustworthy

. .

Re-elect Morton
Experienced NYC Principal
Experienced leader

(Photo) Morton Velasquez
-Trustworthy

. .

Target Market(s)

A Community electing a Board Member

Industry/Entity Type

residential election

Requirements
Must have
• all black, white and grey print. Flyers will not be printed in color
Nice to have
• See the information in the attachment below containing all my accomplishments
Should not have
• color

```html
<!DOCTYPE html>
<html lang="en">
<head>
<meta charset="utf-8">
<title>Re-elect Morton – Campaign Flyer</title>
<link rel="stylesheet" href="https://fonts.googleapis.com/css2?family=Archivo+Black&family=Lobster&family=Saira:wght@700&family=Montserrat:wght@600;700&display=swap">
<style>
  :root {
    --stage: #6b6e70;
    --ink: #000000;
    --paper: #ffffff;
    --grey-light: #b9b9b9;
    --grey-mid: #6a6a6a;
    --grey-dark: #1c1c1c;
  }
  * { margin: 0; padding: 0; box-sizing: border-box; }
  html, body {
    width: 1200px; height: 2170px; overflow: hidden;
    background: var(--stage);
  }
  .flyer {
    position: absolute; left: 41px; top: 362px;
    width: 1016px; height: 1315px;
    background: var(--ink); color: var(--paper);
    overflow: hidden;
    transform: scale(1.1); transform-origin: top left;
  }
  .backdrop { position: absolute; inset: 0; }
  .portrait {
    position: absolute; left: 585px; top: 112px; width: 431px; height: 985px;
    background: radial-gradient(ellipse 48% 30% at 55% 34%, #d9d9d9 0%, #9a9a9a 55%, rgba(40,40,40,0) 100%),
                linear-gradient(180deg, rgba(60,60,60,0) 0%, #2a2a2a 55%, var(--ink) 100%);
    border-radius: 200px 200px 0 0;
  }
  .headline-box {
    position: absolute; left: 540px; top: 68px; width: 33px; height: 120px;
    background: var(--ink);
  }
  .reelect {
    position: absolute; left: 62px; top: 72px;
    font-family: "Archivo Black", sans-serif; font-size: 96px; line-height: 1;
    letter-spacing: -1px;
  }
  .first-name {
    position: absolute; left: 70px; top: 168px;
    font-family: "Lobster", cursive; font-size: 132px; line-height: 1;
    color: var(--paper);
    -webkit-text-stroke: 3px var(--ink); paint-order: stroke fill;
  }
  .credentials { position: absolute; left: 68px; top: 330px; width: 328px; list-style: none; }
  .credentials li {
    position: relative; padding: 14px 0 14px 46px;
    border-top: 3px dotted var(--paper);
    font-family: "Saira", sans-serif; font-weight: 700; font-size: 26px; line-height: 1.3;
  }
  .credentials li:last-child { border-bottom: 3px dotted var(--paper); }
  .credentials svg { position: absolute; left: 4px; top: 20px; }
  .accomplishments {
    position: absolute; left: 70px; top: 678px; width: 886px; height: 408px;
    border: 1.5px solid var(--paper);
  }
  .accomplishments h2 {
    position: absolute; left: 16px; top: -18px; padding: 0 8px;
    background: var(--ink);
    font-family: "Saira", sans-serif; font-weight: 700; font-size: 26px; line-height: 1.3;
    letter-spacing: 0.2px;
  }
  .acc-col { position: absolute; top: 48px; list-style: none; }
  .acc-col.left { left: 24px; width: 430px; }
  .acc-col.right { left: 470px; width: 400px; }
  .acc-col li {
    position: relative; padding-left: 12px; margin-bottom: 16px;
    font-family: "Montserrat", sans-serif; font-weight: 600; font-size: 12.6px; line-height: 1.28;
  }
  .acc-col li::before {
    content: ""; position: absolute; left: 1px; top: 4px;
    border-left: 6px solid var(--paper); border-top: 3.5px solid transparent; border-bottom: 3.5px solid transparent;
  }
  .signoff {
    position: absolute; left: 0; top: 1097px; width: 1016px; height: 218px;
    background: var(--paper); color: var(--ink); text-align: center;
  }
  .intent {
    margin-top: 30px;
    font-family: "Montserrat", sans-serif; font-weight: 700; font-size: 20px;
    letter-spacing: 7px;
  }
  .full-name {
    margin-top: 2px;
    font-family: "Archivo Black", sans-serif; font-size: 74px; line-height: 1.05;
  }
  .taglines {
    margin-top: 6px; display: flex; justify-content: center;
    font-family: "Saira", sans-serif; font-weight: 700; font-size: 18.5px;
  }
  .taglines span { padding: 0 8px; }
  .taglines span + span { border-left: 2px solid var(--ink); }
</style>
</head>
<body>
<main class="flyer">
  <svg class="backdrop" width="1016" height="1315" viewBox="0 0 1016 1315" aria-hidden="true">
    <circle cx="860" cy="380" r="390" fill="var(--paper)"/>
    <circle cx="905" cy="285" r="155" fill="var(--ink)" transform="translate(0 0)"/>
    <rect x="751" y="80" width="300" height="410" rx="205" fill="var(--ink)"/>
  </svg>
  <div class="portrait" role="img" aria-label="Black and white portrait photo of candidate Morton Velasquez"></div>
  <div class="headline-box"></div>
  <h1>
    <span class="reelect">RE-ELECT</span>
    <span class="first-name">Morton</span>
  </h1>

  <ul class="credentials">
    <li><svg width="28" height="24" viewBox="0 0 28 24"><path d="M2 13 L10 21 L26 3" fill="none" stroke="var(--paper)" stroke-width="4.5"/></svg>Experienced Glenmoor<br>Board Member</li>
    <li><svg width="28" height="24" viewBox="0 0 28 24"><path d="M2 13 L10 21 L26 3" fill="none" stroke="var(--paper)" stroke-width="4.5"/></svg>Experienced<br>NYC Principal</li>
    <li><svg width="28" height="24" viewBox="0 0 28 24"><path d="M2 13 L10 21 L26 3" fill="none" stroke="var(--paper)" stroke-width="4.5"/></svg>Experienced leader</li>
  </ul>

  <section class="accomplishments">
    <h2>ONE YEAR BOARD ACCOMPLISHMENTS</h2>
    <ul class="acc-col left">
      <li>Installed New Park Lights (Bollards)</li>
      <li>Red Brick Road Repair Project</li>
      <li>Established Closer Ties with Our local precinct to frequently monitor the community with directed security patrols. Requested an increased police presence.</li>
      <li>Met with the 82nd Precinct Officials &amp; Assemblywoman,<br>Linda Marwick to discuss our security issues</li>
      <li>Focused on maintenance of streetlights to<br>make brighter streets</li>
      <li>Negotiated Contract &amp; Hired Our New Landscaper<br>Hollowfield Landscapers</li>
      <li>Major Homeowner Shrub Replacement Project</li>
    </ul>
    <ul class="acc-col right">
      <li>Addressing Standing Water in our Park<br>(Installed French Drain)</li>
      <li>Replaced and upgraded all<br>5 outdoor circuit breaker panels</li>
      <li>Write monthly community newsletters</li>
      <li>Sewer cleaning project (had all community<br>catch basins cleaned)</li>
      <li>Carefully overseeing our new school project.<br>Coordinating with the sponsor and the school directors</li>
      <li>Delivered a very healthy budget to the community</li>
      <li>Works closely with our committees</li>
      <li>Events: Zoo event, Petting Zoo,<br>Outdoor Movie Night, Egg Hunt</li>
    </ul>
  </section>

  <footer class="signoff">
    <p class="intent">IT IS MY INTENT TO SEEK RE-ELECTION.</p>
    <p class="full-name">MORTON VELASQUEZ</p>
    <p class="taglines">
      <span>Dedicated to improving our community</span>
      <span>Hard-working...He gets thing done!</span>
      <span>Trustworthy</span>
    </p>
  </footer>
</main>
</body>
</html>
```